Business Card Design EFTPOS Comparison site

At QuoteLark.com.au we are a free service that allows our customers to get up to five quotes from our panel of suppliers for a range of BUSINESS related products and services. These products include eftpos / credit card machines, bank accounts, insurance, signage,office furniture etc. basically anything that a small business would need.
The process is done in 3 steps; 1) register your enquiry 2) we source and provide the five cheapest quotes 3) then select the supplier of your choice,the process is simple QuoteLark and is FREE.
Please visit the soon to be revamped website to see our logo.
Target Market(s)
Small business operators
Industry/Entity Type
Small Business
Requirements
Must have
- Double Sided card

```html
<!DOCTYPE html>
<html lang="en">
<head>
<meta charset="utf-8">
<title>QuoteLark Business Card</title>
<link href="https://fonts.googleapis.com/css2?family=Arimo:wght@400;700&display=swap" rel="stylesheet">
<style>
  :root {
    --backdrop: #2a2a2a;
    --card-green: #15973f;
    --card-green-deep: #0f7f33;
    --panel-white: #f7f7f7;
    --brand-orange: #f08a1e;
    --ink-white: #ffffff;
    --ink-black: #111111;
  }
  html, body {
    margin: 0;
    padding: 0;
    width: 1200px;
    height: 900px;
    overflow: hidden;
    background: var(--backdrop);
    font-family: "Arimo", Arial, sans-serif;
  }
  .canvas {
    width: 1200px;
    height: 900px;
    display: flex;
    align-items: center;
    justify-content: center;
    gap: 50px;
  }
  .card {
    width: 500px;
    height: 286px;
    position: relative;
    box-sizing: border-box;
    box-shadow: 0 10px 24px rgba(0,0,0,0.55);
  }
  .card-front {
    background: var(--card-green);
    padding: 22px;
  }
  .front-panel {
    width: 100%;
    height: 100%;
    background: var(--panel-white);
    box-shadow: inset 0 0 14px rgba(0,0,0,0.18);
    display: flex;
    align-items: center;
    justify-content: center;
    gap: 12px;
  }
  .brand-dot {
    width: 30px;
    height: 30px;
    border-radius: 50%;
    background: var(--brand-orange);
  }
  .brand-name {
    font-weight: 700;
    font-size: 48px;
    color: var(--brand-orange);
    letter-spacing: -0.5px;
  }
  .card-back {
    background: linear-gradient(135deg, var(--card-green) 0%, var(--card-green) 60%, var(--card-green-deep) 100%);
  }
  .holder {
    position: absolute;
    left: 52px;
    top: 168px;
    color: var(--ink-white);
  }
  .holder-name {
    font-weight: 700;
    font-size: 25px;
    line-height: 1;
    letter-spacing: 0.5px;
  }
  .holder-name .accent { color: var(--ink-black); }
  .holder-role {
    font-weight: 700;
    font-size: 17px;
    margin-top: 3px;
  }
  .divider {
    position: absolute;
    left: 268px;
    top: 62px;
    width: 2px;
    height: 150px;
    background: var(--ink-black);
  }
  .contacts {
    position: absolute;
    left: 290px;
    top: 68px;
    list-style: none;
    margin: 0;
    padding: 0;
    color: var(--ink-white);
    font-size: 13.5px;
  }
  .contacts li {
    display: flex;
    align-items: center;
    gap: 8px;
    height: 19px;
  }
  .contacts svg { width: 12px; height: 12px; flex: none; }
</style>
</head>
<body>
<main class="canvas">
  <section class="card card-front" aria-label="Card front">
    <div class="front-panel">
      <span class="brand-dot"></span>
      <span class="brand-name">QuoteLark</span>
    </div>
  </section>

  <section class="card card-back" aria-label="Card back">
    <div class="holder">
      <div class="holder-name">YOUR <span class="accent">N</span>AME</div>
      <div class="holder-role">Company Position</div>
    </div>
    <div class="divider"></div>
    <ul class="contacts">
      <li>
        <svg viewBox="0 0 12 12" aria-hidden="true"><circle cx="6" cy="6" r="5.2" fill="none" stroke="#111" stroke-width="1.2"/><path d="M4 3.5 L5 3.5 L5.5 5 L4.8 5.6 Q5.6 7 6.6 7.4 L7.2 6.6 L8.6 7.1 L8.6 8.2 Q5 8.6 3.6 4.4 Z" fill="#111"/></svg>
        000 123 4567
      </li>
      <li>
        <svg viewBox="0 0 12 12" aria-hidden="true"><path d="M6 1 L11.5 6 L9.8 6 L9.8 11 L7.2 11 L7.2 8 L4.8 8 L4.8 11 L2.2 11 L2.2 6 L0.5 6 Z" fill="#111"/></svg>
        your address
      </li>
      <li>
        <svg viewBox="0 0 12 12" aria-hidden="true"><rect x="1" y="3" width="10" height="7" fill="none" stroke="#111" stroke-width="1.2"/><path d="M1 3 L6 7 L11 3" fill="none" stroke="#111" stroke-width="1.2"/></svg>
        youremail@domain.com
      </li>
      <li>
        <svg viewBox="0 0 12 12" aria-hidden="true"><circle cx="6" cy="5" r="4" fill="none" stroke="#111" stroke-width="1.2"/><path d="M2 5 H10 M6 1 V9 M4 11 H8" stroke="#111" stroke-width="1"/></svg>
        QuoteLark.com.au
      </li>
    </ul>
  </section>
</main>
</body>
</html>
```